Velomarket
" Flexible Recruiting Solutions In A Changing World "
Employment
Velomarket is a International Recruitment Agency that makes the world a smaller place. We work both On-Site and Off-Site with our Clients to deliver Employment Services across the Globe. Speed and Flexibility is our aim!
I do not like recruitment websites of people passing documents to each other as I think it is a cliche and is samey. I like slick websites that have their own identity. Harbor Lanterns has a nice website that appeals to their target market and has that feminine touch. Although it is not a Recruitment Website I love the Mabel Quintock site... I like the material grain in the background and would like to have a similar background in white to reflect a business shirt. What I want is to use the Traditional Recruitment Website layout with the JOB SEARCH area and the About Us, Contact Us, Services... tabs... but re-invent it in a way that makes it personal to me.
Exciting
Blue - Matching with logo and images.
Grained White, Material Background (Like a Business Shirt!)
Ideas?
www.mabelquintock.co.uk (Non Recruitment)
www.harbor-lanterns.com (Recruitment)
I would like the look of the website to be Art Deco and inline with the logo. If possible I would like a Deco edging to the tab bar at the top.
There also needs to be a Netlinker & Chirpline icon on the page.
Velomarket Logo
Globe
Main Image

```html
<!DOCTYPE html>
<html lang="en">
<head>
<meta charset="utf-8">
<title>Velomarket — Flexible Recruiting Solutions</title>
<link href="https://fonts.googleapis.com/css2?family=Open+Sans:wght@400;600;700;800&display=swap" rel="stylesheet">
<style>
  :root{
    --navy:#0f2a5c;
    --navy-deep:#0a1f47;
    --blue:#1e5db3;
    --blue-bright:#2a76d2;
    --page:#e6e8ec;
    --page-light:#f4f5f7;
    --white:#ffffff;
    --text:#2b2f38;
    --muted:#6b7280;
    --line:#cdd2da;
  }
  *{box-sizing:border-box;margin:0;padding:0}
  html,body{width:1200px;height:933px;overflow:hidden}
  body{
    font-family:"Open Sans",Arial,sans-serif;
    color:var(--text);
    background:linear-gradient(180deg,var(--page) 0%,var(--page-light) 45%,var(--page) 100%);
    position:relative;
  }
  .topbar{
    position:absolute;left:0;top:0;width:1200px;height:28px;
    background:var(--navy-deep);color:#d8e2f2;font-size:11px;
  }
  .topbar .contact{position:absolute;left:140px;top:0;height:28px;display:flex;gap:26px;align-items:center}
  .topbar .contact span{display:flex;align-items:center;gap:6px}
  .topbar .social{position:absolute;right:140px;top:0;height:28px;display:flex;gap:6px;align-items:center}
  .topbar .social i{display:block;width:16px;height:16px;border-radius:2px;background:var(--blue-bright)}
  .topbar .social span{margin-right:6px}

  .header{position:absolute;left:0;top:28px;width:1200px;height:112px}
  .logo{position:absolute;left:140px;top:18px;display:flex;align-items:center;gap:14px}
  .logo .mark{display:block;width:74px;height:74px;background:var(--navy);border-radius:4px}
  .logo .name{font-size:40px;font-weight:800;color:var(--navy);letter-spacing:1px}
  .nav{position:absolute;left:580px;top:40px;display:flex;align-items:center;gap:28px;font-size:15px;font-weight:700;color:var(--navy)}

  .hero{
    position:absolute;left:181px;top:151px;width:840px;height:328px;
    background:linear-gradient(100deg,#c9a26b 0%,#c9a26b 45%,#dfe8f2 70%,#c8d6e6 100%);
    box-shadow:0 3px 10px rgba(0,0,0,.18);
  }
  .headline{
    position:absolute;left:266px;top:176px;width:380px;
    color:var(--navy-deep);font-weight:700;
  }
  .headline span{display:block;white-space:nowrap}
  .headline .l1{font-size:31px;line-height:38px}
  .headline .l2{font-size:27px;line-height:34px}
  .headline .l3{font-size:22px;line-height:46px}
  .headline .l3 b{font-size:38px;font-weight:700}
  .btn-more{
    position:absolute;left:403px;top:338px;width:116px;height:28px;border-radius:14px;
    background:linear-gradient(180deg,var(--blue-bright),var(--blue));color:#fff;
    font-size:11px;font-weight:800;display:flex;align-items:center;justify-content:center;gap:6px;
  }
  .globe{
    position:absolute;left:870px;top:270px;width:190px;height:200px;border-radius:8px;
    background:linear-gradient(160deg,#b9d4f0 0%,#2a76d2 55%,#1a4d96 100%);
  }

  .panel{
    position:absolute;left:100px;top:500px;width:1000px;height:308px;
    background:var(--white);box-shadow:0 2px 8px rgba(0,0,0,.1);
  }
  .employers{
    position:absolute;left:130px;top:530px;width:300px;height:252px;
    background:var(--white);border:1px solid var(--line);
  }
  .ribbon{
    position:absolute;left:-20px;top:22px;width:150px;height:30px;
    background:var(--blue);color:#fff;font-size:14px;font-weight:800;line-height:30px;text-align:center;
    transform:rotate(-32deg);transform-origin:center;
    box-shadow:0 2px 4px rgba(0,0,0,.2);
  }
  .employers .intro{position:absolute;left:108px;top:42px;width:180px;font-size:15px;font-weight:700;color:var(--navy);line-height:19px}
  .brands{position:absolute;left:24px;top:124px;display:grid;grid-template-columns:repeat(3,70px);gap:14px 16px}
  .brands i{display:block;height:22px;border-radius:11px;background:#d7dde6}
  .btn-view{
    position:absolute;left:98px;top:206px;width:106px;height:30px;border:1px solid #b9c0cb;border-radius:4px;
    background:linear-gradient(180deg,#fff,#e4e7ec);font-size:12px;font-weight:700;color:var(--muted);
    display:flex;align-items:center;justify-content:center;
  }

  .jobs{position:absolute;left:455px;top:530px;width:598px;height:252px;border:1px solid var(--line);background:var(--white)}
  .tabs{display:flex;height:40px;border-bottom:1px solid var(--line);background:#eef0f3}
  .tabs div{display:flex;align-items:center;justify-content:center;font-size:15px;color:var(--navy);border-right:1px solid var(--line)}
  .tabs .active{width:250px;background:var(--white);margin-bottom:-1px}
  .tabs .active b{font-weight:800;margin-left:4px}
  .tabs div:nth-child(2){width:160px}
  .tabs div:nth-child(3){flex:1;border-right:0}
  .cols{display:flex;padding:14px 0 0 26px;gap:18px;font-size:10.5px;line-height:14px}
  .cols ul{list-style:none;width:128px}
  .cols li.head{font-weight:800;color:var(--navy)}
  .cols li.gap{height:8px}
  .pager{position:absolute;right:22px;bottom:18px;font-size:11px;color:var(--blue)}

  .footer{
    position:absolute;left:75px;top:812px;width:1045px;height:58px;
    background:linear-gradient(180deg,var(--blue) 0%,var(--navy) 100%);color:#e4ecf8;
  }
  .footer .flogo{position:absolute;left:64px;top:12px;display:flex;align-items:center;gap:8px}
  .footer .flogo i{display:block;width:34px;height:34px;background:#fff;opacity:.9;border-radius:3px}
  .footer .flogo span{font-size:19px;font-weight:800;color:#fff}
  .footer .legal{position:absolute;left:255px;top:15px;font-size:11px;line-height:15px}
  .footer .links{position:absolute;right:56px;top:15px;font-size:11px}
</style>
</head>
<body>
  <div class="topbar">
    <div class="contact">
      <span><svg width="12" height="12" viewBox="0 0 12 12"><path d="M3 1l2 2-1 2c1 2 2 3 3 3l2-1 2 2-1 2C5 11 1 7 1 2z" fill="#d8e2f2"/></svg>+xx (x) xxxxxxx xxx</span>
      <span><svg width="13" height="10" viewBox="0 0 13 10"><rect x=".5" y=".5" width="12" height="9" fill="none" stroke="#d8e2f2"/><path d="M.5.5l6 5 6-5" fill="none" stroke="#d8e2f2"/></svg>info@velomarket.com</span>
    </div>
    <div class="social"><span>Social Networks</span><i aria-label="Social network"></i><i aria-label="Chirpline"></i><i aria-label="Netlinker"></i></div>
  </div>

  <div class="header">
    <div class="logo"><i class="mark"></i><span class="name">VELOMARKET</span></div>
    <nav class="nav">
      <svg width="26" height="22" viewBox="0 0 26 22"><path d="M13 1L1 11h4v10h6v-6h4v6h6V11h4z" fill="#1e5db3"/></svg>
      <span>About us</span><span>Services</span><span>Find Jobs</span><span>Post CV</span><span>Contact Us</span>
    </nav>
  </div>

  <section class="hero" role="img" aria-label="Photo of two pairs of hands passing a cardboard sign"></section>
  <h1 class="headline">
    <span class="l1">Flexible</span>
    <span class="l2">Recruiting Solutions</span>
    <span class="l3">in a <b>Changing World</b></span>
  </h1>
  <div class="btn-more">KNOW MORE <span>»</span></div>
  <div class="globe" role="img" aria-label="Illustration of a globe made of puzzle pieces"></div>

  <div class="panel"></div>

  <section class="employers">
    <div class="ribbon">TOP EMPLOYERS!</div>
    <p class="intro">Lorem ipsum dolor sit amet adipiscing elit dolor ipsum.</p>
    <div class="brands"><i></i><i></i><i></i><i></i><i></i><i></i></div>
    <div class="btn-view">VIEW ALL</div>
  </section>

  <section class="jobs">
    <div class="tabs"><div class="active">Browse Jobs by <b>Specialization</b></div><div>Locations</div><div>Position Levels</div></div>
    <div class="cols">
      <ul><li class="head">Accounting / Finance</li><li>General/Cost Acct (2148)</li><li>Banking/Financial (647)</li><li>Audit &amp; Taxation (426)</li><li>Finance/Investment (184)</li><li class="gap"></li><li class="head">Admin / HR</li><li>Human Resources (1348)</li></ul>
      <ul><li>Clerical/Admin (1113)</li><li>Secretarial (382)</li><li>Top Management (129)</li><li class="gap"></li><li class="head">Sales / Marketing</li><li>Marketing (1441)</li><li>Sales-Retail/General (116)</li><li>Sales-Corporate (852)</li></ul>
      <ul><li>Telesales/Telemarketing (74)</li><li>Sales-Eng/Tech/IT (366)</li><li>Sales-Financial Services (15)</li><li>Merchandising (117)</li><li class="gap"></li><li class="head">Arts / Media / Comm</li><li>Arts/Creative Design (654)</li><li>Advertising (267)</li></ul>
      <ul><li>Public Relations (124)</li><li>Entertainment (69)</li><li class="gap"></li><li class="head">Services</li><li>Customer Service (5728)</li><li>Tech &amp; Helpdesk Support (766)</li></ul>
    </div>
    <div class="pager">1 2 3 4 5 last &gt;&gt;</div>
  </section>

  <footer class="footer">
    <div class="flogo"><i></i><span>VELOMARKET</span></div>
    <div class="legal">© 2011 Velomarket<br>Terms &amp; Conditions | FAQ'S | Contact Us</div>
    <div class="links">Home | About Us | Services | Find Jobs | Post CV | Contact Us</div>
  </footer>
</body>
</html>
```